Flyer Design / Authenticity Certificate - Art Work

Looking for a design of a "Authenticity Certificate" - flyer, that will include some basic company info like logo etc, and allow our in house artist to sign and authenticate before it is applied the reverse of one of the paintings we will sell. Linked with our online sales website - "Amber Harbor Studios", where we recreate one off oil paintings from digital photographs. Our business logo should be incorporated in the design, along with a section for "Artisit Name" "Artisit Signature" "Ref Code"
Updates

Hi.. Sorry I should have added the size we need - please design accordingly to A6. Thanks.

Industry/Entity Type

It Company

Font styles to use
Serif
Script

Colors

Designer to choose colors to be used in the design.

Requirements
Must have
• Company logo
• Area for artist to print and sign
• Area for a reference
Nice to have
• must use the logo, maybe incorporate a "seal" icon, like what was used as a wax seal on older style documents

```html
<!DOCTYPE html>
<html lang="en">
<head>
<meta charset="utf-8">
<title>Certificate of Authenticity – Amber Harbor Studios</title>
<link rel="stylesheet" href="https://fonts.googleapis.com/css2?family=Great+Vibes&family=Merriweather:wght@300;400;700&display=swap">
<style>
  :root {
    --paper: #ffffff;
    --frame-gold: #dcc08e;
    --frame-gold-light: #ecdcbc;
    --ink: #3a3a3a;
    --ink-strong: #2a2a2a;
    --title-red: #d8324f;
    --ribbon-light: #668f8a;
    --ribbon-dark: #456d69;
    --wax-light: #b5182a;
    --wax-dark: #7d0d18;
    --mark-dark: #2b2b2b;
  }
  html, body {
    margin: 0;
    padding: 0;
    width: 1200px;
    height: 852px;
    overflow: hidden;
    background: var(--paper);
  }
  .certificate {
    position: relative;
    width: 1200px;
    height: 852px;
    background: var(--paper);
    font-family: "Merriweather", Georgia, serif;
    color: var(--ink);
  }
  .ornamental-frame {
    position: absolute;
    left: 20px;
    top: 20px;
    width: 1160px;
    height: 812px;
    background: linear-gradient(135deg, var(--frame-gold-light), var(--frame-gold) 50%, var(--frame-gold-light));
  }
  .frame-inner {
    position: absolute;
    left: 88px;
    top: 88px;
    width: 1024px;
    height: 676px;
    background: var(--paper);
  }
  .ribbon {
    position: absolute;
    left: 162px;
    top: 0;
    width: 120px;
    height: 560px;
    filter: drop-shadow(3px 3px 4px rgba(0,0,0,0.25));
  }
  .wax-seal {
    position: absolute;
    left: 126px;
    top: 232px;
    width: 196px;
    height: 196px;
    filter: drop-shadow(3px 4px 5px rgba(0,0,0,0.3));
  }
  .ref-code {
    position: absolute;
    left: 828px;
    top: 112px;
    font-size: 20px;
    font-weight: 700;
    color: var(--ink-strong);
    white-space: nowrap;
  }
  .ref-code .fill-line {
    display: inline-block;
    width: 140px;
    border-bottom: 2px dotted var(--ink);
    margin-left: 6px;
  }
  .title {
    position: absolute;
    left: 352px;
    top: 168px;
    margin: 0;
    font-family: "Great Vibes", cursive;
    font-weight: 400;
    font-size: 70px;
    line-height: 1;
    color: var(--title-red);
    white-space: nowrap;
  }
  .statement {
    position: absolute;
    left: 366px;
    top: 304px;
    width: 700px;
    margin: 0;
    font-size: 20px;
    font-weight: 300;
    line-height: 30px;
  }
  .artist-name-line {
    position: absolute;
    left: 370px;
    top: 416px;
    width: 682px;
    border-top: 2px dashed var(--ink);
  }
  .seller {
    position: absolute;
    left: 366px;
    top: 458px;
    margin: 0;
    font-size: 20px;
    font-weight: 300;
    white-space: nowrap;
  }
  .seller strong {
    font-weight: 700;
    color: var(--ink-strong);
  }
  .brand {
    position: absolute;
    left: 780px;
    top: 556px;
    width: 284px;
    text-align: center;
  }
  .brand-dot {
    display: block;
    width: 112px;
    height: 112px;
    margin: 0 auto 18px;
    border-radius: 50%;
    background: var(--mark-dark);
  }
  .brand-name {
    font-size: 20px;
    font-weight: 700;
    letter-spacing: 1px;
    color: var(--mark-dark);
    white-space: nowrap;
  }
  .signature {
    position: absolute;
    left: 162px;
    top: 684px;
    width: 216px;
  }
  .signature-line {
    border-top: 2px dashed var(--ink);
  }
  .signature-label {
    margin-top: 10px;
    font-size: 19px;
    font-weight: 300;
    white-space: nowrap;
  }
</style>
</head>
<body>
<main class="certificate">
  <div class="ornamental-frame" role="img" aria-label="Gold filigree ornamental border framing the certificate"></div>
  <div class="frame-inner"></div>

  <svg class="ribbon" viewBox="0 0 120 560" aria-hidden="true">
    <defs>
      <linearGradient id="ribbonShade" x1="0" y1="0" x2="0" y2="1">
        <stop offset="0" stop-color="var(--ribbon-dark)"/>
        <stop offset="0.35" stop-color="var(--ribbon-light)"/>
        <stop offset="1" stop-color="var(--ribbon-dark)"/>
      </linearGradient>
    </defs>
    <polygon points="0,0 120,0 120,560 60,504 0,560" fill="url(#ribbonShade)"/>
  </svg>

  <svg class="wax-seal" viewBox="0 0 196 196" aria-hidden="true">
    <defs>
      <radialGradient id="waxShade" cx="0.45" cy="0.4" r="0.6">
        <stop offset="0" stop-color="var(--wax-light)"/>
        <stop offset="1" stop-color="var(--wax-dark)"/>
      </radialGradient>
    </defs>
    <circle cx="98" cy="98" r="96" fill="url(#waxShade)"/>
  </svg>

  <div class="ref-code">Ref. Code :<span class="fill-line"></span></div>

  <h1 class="title">Certificate of Authenticity</h1>

  <p class="statement">This is to certify that the painting you purchased is authentic and original painting created by</p>

  <div class="artist-name-line"></div>

  <p class="seller">and purchased from <strong>AMBER HARBOR STUDIOS PVT. LTD.</strong></p>

  <div class="brand">
    <span class="brand-dot"></span>
    <div class="brand-name">AMBER HARBOR STUDIOS</div>
  </div>

  <div class="signature">
    <div class="signature-line"></div>
    <div class="signature-label">ARTIST SIGNATURE</div>
  </div>
</main>
</body>
</html>
```